Criação de Papelaria (6 itens) para Lumiar & Castelo
A empresa queria:
" EMPRESA FAMILIAR PRODUTORA DE GRÃOS hA 34 ANOS NO MERCADO, PIONEIRA EM IRRIGAÇÃO TIPO PIVO CENTRAL. "

```html
<!DOCTYPE html>
<html lang="pt-BR">
<head>
<meta charset="UTF-8">
<title>Lumiar &amp; Castelo — Assinatura</title>
<link href="https://fonts.googleapis.com/css2?family=Cormorant+Garamond:wght@500&family=Questrial&display=swap" rel="stylesheet">
<style>
  :root {
    --gold: #b8995a;
    --gold-dark: #a8894a;
    --ink: #3a3a3a;
    --grey: #7a7a7a;
    --paper: #ffffff;
    --backdrop: #e6e6e6;
  }
  * { box-sizing: border-box; margin: 0; padding: 0; }
  html, body { width: 1200px; height: 1200px; overflow: hidden; }
  body {
    background: var(--backdrop);
    display: flex; align-items: center; justify-content: center;
    font-family: "Questrial", sans-serif;
  }
  .signature-strip {
    position: relative;
    width: 1040px; height: 230px;
    background: var(--paper);
    border-radius: 16px 16px 0 0;
    box-shadow: 0 6px 18px rgba(0,0,0,.12);
    display: flex; align-items: center;
    padding: 0 28px 14px 60px;
  }
  .signature-strip::after {
    content: ""; position: absolute; left: 0; right: 0; bottom: 0;
    height: 16px; background: var(--gold);
  }
  .brand { display: flex; align-items: center; gap: 16px; width: 370px; }
  .brand-dot { width: 46px; height: 46px; border-radius: 50%; background: var(--gold); flex: none; }
  .brand-name {
    font-family: "Cormorant Garamond", serif; font-weight: 500;
    font-size: 36px; line-height: 1.0; color: var(--grey);
  }
  .person {
    border-left: 6px solid var(--gold);
    padding-left: 14px; height: 66px;
    display: flex; flex-direction: column; justify-content: center;
  }
  .person-name { font-size: 30px; color: var(--gold-dark); line-height: 1.1; }
  .person-role { font-size: 19px; color: var(--grey); line-height: 1.1; margin-left: 20px; }
  .contacts { margin-left: auto; display: flex; flex-direction: column; gap: 8px; }
  .contact { display: flex; align-items: center; justify-content: flex-end; gap: 12px; }
  .contact-text { font-size: 14px; line-height: 1.25; color: var(--ink); text-align: right; }
  .contact-icon {
    width: 22px; height: 22px; flex: none; background: var(--gold);
    border-radius: 3px; display: flex; align-items: center; justify-content: center;
  }
  .contact-icon svg { width: 14px; height: 14px; fill: #fff; }
  .contact-address .contact-text { line-height: 1.3; }
</style>
</head>
<body>
  <div class="signature-strip">
    <div class="brand">
      <span class="brand-dot"></span>
      <span class="brand-name">Lumiar &amp;<br>Castelo</span>
    </div>
    <div class="person">
      <span class="person-name">Nome e Sobrenome</span>
      <span class="person-role">Cargo/Função</span>
    </div>
    <div class="contacts">
      <div class="contact">
        <span class="contact-text">(00) 0000-0000</span>
        <span class="contact-icon"><svg viewBox="0 0 24 24"><path d="M6.6 10.8a15 15 0 0 0 6.6 6.6l2.2-2.2a1 1 0 0 1 1-.25 11.4 11.4 0 0 0 3.6.6 1 1 0 0 1 1 1V20a1 1 0 0 1-1 1A17 17 0 0 1 3 4a1 1 0 0 1 1-1h3.5a1 1 0 0 1 1 1c0 1.25.2 2.45.6 3.6a1 1 0 0 1-.25 1z"/></svg></span>
      </div>
      <div class="contact">
        <span class="contact-text">Contato@exemplo.com</span>
        <span class="contact-icon"><svg viewBox="0 0 24 24"><path d="M3 6h18v12H3z" fill="none" stroke="#fff" stroke-width="2"/><path d="M3 6l9 7 9-7" fill="none" stroke="#fff" stroke-width="2"/></svg></span>
      </div>
      <div class="contact contact-address">
        <span class="contact-text">Rua exemplo, 000<br>Cidade - UF, CEP: 00000-000</span>
        <span class="contact-icon"><svg viewBox="0 0 24 24"><path d="M12 2a7 7 0 0 0-7 7c0 5.2 7 13 7 13s7-7.8 7-13a7 7 0 0 0-7-7zm0 9.5A2.5 2.5 0 1 1 12 6.5a2.5 2.5 0 0 1 0 5z"/></svg></span>
      </div>
      <div class="contact">
        <span class="contact-text">social.exemplo/empresa</span>
        <span class="contact-icon"></span>
      </div>
    </div>
  </div>
</body>
</html>
```